4K Business Card Design

We need a business card that emphasizes consulting services worldwide. The name of the company is KKKK Consulting Group. We provide consulting services across several industries including but not limited to commodities, telecom, manufacturing, logistics, marketing and operations. We would like to see a creative design that emphasizes the global aspect, including Latin America and US markets, as well the bilingual nature of the service offerings.

The contact information section should include icons to represent the following data:
1) Name, Title and Company Name
2) Mobile Number
3) Skype ID
4) Email
5) Web Page
6) Location

We would like to see a card that emphasizes the worldwide concept. The back of the card should be simple, including only the logo (or a portion of the logo) and the slogan.

We would also like to see business cards in a booklet format. The colors to be used should be the same combination of colors used in the logos attached to this brief.

The logo design and some business card examples from Artful Herd are attached for reference on style and look.

Target Market(s)

International business executives, 45-65 years of age, bilingual

Industry/Entity Type

Marketing

Colors
0792cd
34a7d8
85cae6
ffffff
cee9f5
ecf7fb

Requirements
Must have
• Please follow colors in logo attached.

2) Mobile Number
3) Skype ID
4) Email
5) Web Page
6) Location
Nice to have
• Global concept, consulting profile, diverse industry focus
Should not have
• No black color

```html
<!DOCTYPE html>
<html lang="en">
<head>
<meta charset="utf-8">
<title>KKKK Consulting Group – Business Card</title>
<link rel="stylesheet" href="https://fonts.googleapis.com/css2?family=Anton&family=Oswald:wght@600&family=Montserrat:wght@600&family=Didact+Gothic&display=swap">
<style>
  :root {
    --brand-blue: #1592cd;
    --mid-blue: #34a7d8;
    --soft-blue: #85cae6;
    --pale-blue: #cee9f5;
    --white: #ffffff;
    --logo-grey: #879694;
    --logo-cube: #8cbde0;
    --slogan-blue: #5f95bd;
    --trim-red: #d8282f;
    --label-ink: #000000;
    --sheet-border: #222222;
  }
  * { box-sizing: border-box; margin: 0; padding: 0; }
  html, body { width: 849px; height: 1200px; overflow: hidden; background: var(--white); }
  .sheet {
    position: relative; width: 849px; height: 1200px;
    border: 2px solid var(--sheet-border); background: var(--white);
  }
  .side-label {
    position: absolute; left: 0; width: 100%; text-align: center;
    font-family: "Anton", sans-serif; font-size: 76px; line-height: 1;
    color: var(--label-ink); letter-spacing: 1px;
  }
  .side-label--back { top: 46px; }
  .side-label--front { top: 1072px; }

  .card { position: absolute; left: 49px; width: 751px; overflow: hidden; }
  .card--back { top: 163px; height: 424px; background: var(--white); }
  .card--front { top: 613px; height: 450px; background: var(--brand-blue); }

  .card__art { position: absolute; inset: 0; }

  .trim { position: absolute; pointer-events: none; }
  .trim--bleed { border: 2px solid var(--trim-red); }
  .trim--safe { border: 2px solid var(--mid-blue); }
  .card--back .trim--bleed { left: 27px; top: 0; width: 697px; height: 398px; }
  .card--back .trim--safe { left: 40px; top: 13px; width: 671px; height: 372px; }
  .card--front .trim--bleed { left: 27px; top: 24px; width: 697px; height: 399px; }
  .card--front .trim--safe { left: 40px; top: 38px; width: 671px; height: 372px; }

  .brand { position: absolute; display: flex; align-items: center; }
  .brand__mark { background: var(--logo-cube); flex: none; }
  .brand__name {
    font-family: "Montserrat", sans-serif; font-weight: 600;
    color: var(--logo-grey); line-height: 1.05; text-transform: uppercase;
  }
  .card--back .brand { left: 80px; top: 68px; gap: 10px; }
  .card--back .brand__mark { width: 72px; height: 72px; }
  .card--back .brand__name { font-size: 29px; }

  .front-panel {
    position: absolute; left: 54px; top: 51px; width: 644px; height: 345px;
    background: var(--white);
  }
  .card--front .brand { left: 46px; top: 112px; gap: 18px; }
  .card--front .brand__mark { width: 136px; height: 126px; }
  .card--front .brand__name { font-size: 48px; }
  .slogan {
    position: absolute; left: 0; width: 100%; top: 272px; text-align: center;
    font-family: "Didact Gothic", sans-serif; font-size: 19px; letter-spacing: 0.5px;
    color: var(--slogan-blue);
  }

  .contact { position: absolute; color: var(--white); font-family: "Didact Gothic", sans-serif; }
  .icon { width: 15px; height: 15px; flex: none; fill: var(--white); }
  .contact__person { left: 60px; top: 247px; }
  .contact__name, .contact__company {
    font-family: "Oswald", sans-serif; font-weight: 600; font-size: 27px;
    line-height: 1.1; text-transform: uppercase; letter-spacing: 0.3px;
  }
  .contact__name { display: flex; align-items: center; gap: 8px; }
  .contact__name .icon { width: 20px; height: 20px; }
  .contact__role { font-size: 15px; margin-top: 1px; display: flex; align-items: center; gap: 6px; }
  .contact__company { margin-top: 16px; }
  .contact__details { right: 73px; top: 279px; font-size: 16px; line-height: 25px; }
  .contact__row { display: flex; align-items: center; justify-content: flex-end; gap: 8px; }
</style>
</head>
<body>
<main class="sheet">
  <h1 class="side-label side-label--back">BACK</h1>

  <section class="card card--back" aria-label="Card back">
    <svg class="card__art" viewBox="0 0 751 424" preserveAspectRatio="none" aria-hidden="true">
      <path d="M0 204 C 250 200, 500 150, 751 50 L751 424 L0 424 Z" fill="var(--pale-blue)"/>
      <path d="M0 217 C 260 212, 500 170, 751 110 L751 424 L0 424 Z" fill="var(--soft-blue)"/>
      <path d="M0 233 C 260 230, 520 210, 751 177 L751 424 L0 424 Z" fill="var(--brand-blue)"/>
    </svg>

    <div class="brand">
      <span class="brand__mark"></span>
      <span class="brand__name">4K Consulting<br>Group</span>
    </div>

    <div class="contact contact__person">
      <p class="contact__name">
        <svg class="icon" viewBox="0 0 16 16" aria-hidden="true"><circle cx="8" cy="4.5" r="3.5"/><path d="M1 16c0-4 3-6.5 7-6.5s7 2.5 7 6.5z"/></svg>
        Elena Torrado
      </p>
      <p class="contact__role">President &amp; CEO</p>
      <p class="contact__company">KKKK Consulting Group</p>
      <p class="contact__role">
        <svg class="icon" viewBox="0 0 16 16" aria-hidden="true"><path d="M8 0a5.5 5.5 0 0 0-5.5 5.5C2.5 10 8 16 8 16s5.5-6 5.5-10.5A5.5 5.5 0 0 0 8 0zm0 7.7a2.2 2.2 0 1 1 0-4.4 2.2 2.2 0 0 1 0 4.4z"/></svg>
        Palm Vista, FL
      </p>
    </div>

    <div class="contact contact__details">
      <p class="contact__row">
        <svg class="icon" viewBox="0 0 16 16" aria-hidden="true"><rect x="4" y="0.5" width="8" height="15" rx="1.5"/><rect x="5.5" y="2.5" width="5" height="9" fill="var(--brand-blue)"/></svg>
        Mobile: +1 305 555-0184
      </p>
      <p class="contact__row">
        <svg class="icon" viewBox="0 0 16 16" aria-hidden="true"><path d="M0 3h16v10H0z"/><path d="M0.8 3.8 8 9l7.2-5.2" fill="none" stroke="var(--brand-blue)" stroke-width="1.4"/></svg>
        Email: k4cg@mailbox.com
      </p>
      <p class="contact__row">
        <svg class="icon" viewBox="0 0 16 16" aria-hidden="true"><path d="M1 1.5h14v9.5H6l-4 3.5v-3.5H1z"/></svg>
        Skype ID: k4consultinggroup
      </p>
      <p class="contact__row">
        <svg class="icon" viewBox="0 0 16 16" aria-hidden="true"><g fill="none" stroke="var(--white)" stroke-width="1.3"><circle cx="8" cy="8" r="7"/><ellipse cx="8" cy="8" rx="3" ry="7"/><path d="M1 8h14M2.2 4.5h11.6M2.2 11.5h11.6"/></g></svg>
        Web: www.k4consulting.com
      </p>
    </div>

    <div class="trim trim--bleed"></div>
    <div class="trim trim--safe"></div>
  </section>

  <section class="card card--front" aria-label="Card front">
    <div class="trim trim--bleed"></div>
    <div class="trim trim--safe"></div>
    <div class="front-panel">
      <div class="brand">
        <span class="brand__mark"></span>
        <span class="brand__name">4K Consulting<br>Group</span>
      </div>
      <p class="slogan">Global Consulting · Consultoría Global</p>
    </div>
  </section>

  <h2 class="side-label side-label--front">FRONT</h2>
</main>
</body>
</html>
```